BRIMWAVE.live*

I am needing a web site built for the main purpose of uploading podcasts
(MP3 files) to be viewed by large audiences of 1000+ site visitors on a regular basis. I have created a rough draft of how I want the site to look.

i have created a rough draft of the home page - the LOGO for this site is a spectacular lightening bolt which appears on my home page sample... the file for this image I purchased is too large to download to your site. I will supply on reuquest.

There will be 5 pages; HOME ABOUT RESOURCES DEVOTIONALS MORTY.
I have all the content prepared for each of the above pages.

Target Market(s)

All people groups seeking positive and encouraging words, life lessons and testimonies of faith.

Coding

Coded - Design and coding required

Number of Pages Required

1 page

Colors
3176b5

Requirements
Must have
• The design and layout provided - my sample

Black backgrounds as shown on my sample

```html
<!DOCTYPE html>
<html lang="en">
<head>
<meta charset="utf-8">
<title>BRIMWAVE.live — Resources</title>
<link rel="stylesheet" href="https://fonts.googleapis.com/css2?family=Playfair+Display:wght@700;900&family=Montserrat:wght@400;600;700&family=Open+Sans:wght@400&display=swap">
<style>
  :root {
    --black: #000000;
    --white: #ffffff;
    --hero-deep: #021040;
    --hero-mid: #0a2a9a;
    --hero-glow: #1fa8ff;
    --accent-cyan: #19c6f0;
    --submit-blue: #0b3cf5;
    --cover-sand: #b89a68;
    --cover-dark: #4a3a28;
    --grey-text: #e6e6e6;
  }
  * { margin: 0; padding: 0; box-sizing: border-box; }
  html, body { width: 1130px; height: 1200px; overflow: hidden; background: var(--black); }
  .page { position: relative; width: 1130px; height: 1200px; background: var(--black); color: var(--white); overflow: hidden; }

  .hero {
    position: absolute; left: 0; top: 0; width: 1130px; height: 483px;
    background:
      radial-gradient(ellipse 260px 120px at 420px 280px, rgba(31,168,255,0.55), transparent 70%),
      radial-gradient(ellipse 200px 160px at 1040px 390px, rgba(31,168,255,0.45), transparent 70%),
      linear-gradient(135deg, var(--hero-mid) 0%, var(--hero-deep) 55%, #020a2a 100%);
  }
  .nav-link {
    position: absolute; top: 48px;
    font-family: 'Playfair Display', serif; font-weight: 700; font-size: 13.5px;
    color: var(--white); text-decoration: none; letter-spacing: 0.2px;
  }
  .nav-link.is-active::after {
    content: ""; position: absolute; left: 50%; top: 27px; width: 24px; height: 2px;
    margin-left: -12px; background: var(--accent-cyan);
  }
  .brand {
    position: absolute; left: 557px; top: 30px; transform: translateX(-50%);
    font-family: 'Playfair Display', serif; font-weight: 900; font-size: 40px;
    color: var(--white); white-space: nowrap; letter-spacing: 0.5px;
  }
  .hero-title {
    position: absolute; left: 574px; top: 222px; transform: translateX(-50%);
    font-family: 'Playfair Display', serif; font-weight: 900; font-size: 78px;
    line-height: 1; color: var(--white); letter-spacing: -1px;
  }

  .offer-cover {
    position: absolute; left: 153px; top: 582px; width: 227px; height: 326px;
    border: 2px solid var(--white);
    background: linear-gradient(180deg, var(--cover-sand) 0%, #c9ad7c 45%, #7a6444 70%, var(--cover-dark) 100%);
  }
  .offer-text {
    position: absolute; left: 428px; top: 578px; width: 560px;
    font-family: 'Montserrat', sans-serif; font-weight: 400; font-size: 16px; line-height: 25.5px;
    color: var(--white);
  }
  .field {
    position: absolute; left: 431px; width: 470px; height: 46px;
    border: 1px solid var(--white); background: var(--black);
    font-family: 'Montserrat', sans-serif; font-weight: 600; font-size: 12.5px;
    color: var(--white); padding-left: 20px; line-height: 44px;
  }
  .field-name { top: 659px; }
  .field-address { top: 724px; }
  .field-email { top: 790px; }
  .submit-button {
    position: absolute; left: 431px; top: 853px; width: 156px; height: 49px;
    background: var(--submit-blue); color: var(--white);
    font-family: 'Montserrat', sans-serif; font-weight: 700; font-size: 16px;
    text-align: center; line-height: 49px; letter-spacing: 0.3px;
  }

  .footer-glow-left {
    position: absolute; left: -80px; top: 980px; width: 280px; height: 260px;
    background: radial-gradient(ellipse at 40% 60%, rgba(120,120,120,0.35), transparent 65%);
  }
  .footer-glow-right {
    position: absolute; right: -60px; top: 960px; width: 260px; height: 240px;
    background: radial-gradient(ellipse at 60% 40%, rgba(120,120,120,0.3), transparent 65%);
  }
  .social-row { position: absolute; left: 485px; top: 1014px; }
  .footer-link {
    position: absolute; top: 1066px;
    font-family: 'Playfair Display', serif; font-weight: 700; font-size: 15px;
    color: var(--white); text-decoration: none;
  }
  .copyright {
    position: absolute; left: 554px; top: 1101px; transform: translateX(-50%);
    font-family: 'Open Sans', sans-serif; font-size: 13px; color: var(--grey-text); white-space: nowrap;
  }
</style>
</head>
<body>
<div class="page">
  <header class="hero" role="img" aria-label="Glowing blue lightning bolt artwork on a deep blue background">
    <a class="nav-link" style="left:79px" href="#">HOME</a>
    <a class="nav-link" style="left:166px" href="#">ABOUT</a>
    <a class="nav-link" style="left:258px" href="#">MORTY</a>
    <div class="brand">BRIMWAVE.live</div>
    <a class="nav-link is-active" style="left:811px" href="#">RESOURCES</a>
    <a class="nav-link" style="left:936px" href="#">DEVOTIONALS</a>
    <h1 class="hero-title">RESOURCES</h1>
  </header>

  <main>
    <div class="offer-cover" role="img" aria-label="Pocket bible cover showing motorcycle gauges on an open desert highway"></div>
    <p class="offer-text">While quantities last, we are offering FREE biker pocket bibles. Simply fill out the form below and we’ll pop one in the mail for you.</p>
    <div class="field field-name">Name</div>
    <div class="field field-address">Mailing address</div>
    <div class="field field-email">Email</div>
    <div class="submit-button">SUBMIT</div>
  </main>

  <footer>
    <div class="footer-glow-left" role="img" aria-label="Faint grey lightning decoration"></div>
    <div class="footer-glow-right" role="img" aria-label="Faint grey lightning decoration"></div>
    <svg class="social-row" width="140" height="34" viewBox="0 0 140 34" aria-label="Social links">
      <g fill="none" stroke="#ffffff" stroke-width="1.5">
        <circle cx="17" cy="17" r="15.5"/>
        <circle cx="52" cy="17" r="15.5"/>
        <circle cx="87" cy="17" r="15.5"/>
        <circle cx="122" cy="17" r="15.5"/>
      </g>
    </svg>
    <a class="footer-link" style="left:282px" href="#">HOME</a>
    <a class="footer-link" style="left:378px" href="#">ABOUT</a>
    <a class="footer-link" style="left:480px" href="#">MORTY</a>
    <a class="footer-link" style="left:583px" href="#">RESOURCES</a>
    <a class="footer-link" style="left:720px" href="#">DEVOTIONALS</a>
    <p class="copyright">© 2020 Company Name&nbsp;|&nbsp;All Rights Reserved</p>
  </footer>
</div>
</body>
</html>
```